Project Brightvale Wellness

We need a business/ logo card design for our company based out of Canada. We will be retailing cannibus products to our customers.
For colors I've found this online : https://www.huetrackr.example/palette-results/?colors=70ff02,ff0270,ff4a02,02e1ff . We especially like the green and blue .
We would like our business card design to communicate modern medicine .

Target Market(s)

males 20-40 years

Industry/Entity Type

Health And Wellness

Contact Information for Business Card

Address is : 248 Dunmore Ave E
Toronto, ON K7R 3T8
website: www.brightvalewellness.example

Font styles to use
Serif

Requirements
Must have
• clear, easy to read logo
Nice to have
• contrasting colors
Should not have
• we want to stay away from marijuana leaf

```html
<!DOCTYPE html>
<html lang="en">
<head>
<meta charset="utf-8">
<title>Brightvale Wellness – Business Card</title>
<link href="https://fonts.googleapis.com/css2?family=Cinzel:wght@400&family=Open+Sans:wght@400;600&display=swap" rel="stylesheet">
<style>
  :root {
    --backdrop: #262626;
    --card-light: #dcbb94;
    --card-mid: #c9a377;
    --card-dark: #a87d52;
    --ink: #1e1a16;
    --rule: rgba(30, 26, 22, 0.45);
  }
  html, body {
    margin: 0;
    padding: 0;
    width: 1200px;
    height: 900px;
    overflow: hidden;
    background: var(--backdrop);
  }
  .canvas {
    position: relative;
    width: 1200px;
    height: 900px;
  }
  .card {
    position: absolute;
    top: 307px;
    width: 438px;
    height: 270px;
    background: linear-gradient(160deg, var(--card-light) 0%, var(--card-mid) 55%, var(--card-dark) 100%);
    color: var(--ink);
  }
  .card--front { left: 150px; }
  .card--back { left: 610px; }

  .wordmark {
    position: absolute;
    left: 0;
    right: 0;
    text-align: center;
    font-family: "Cinzel", "Trajan Pro", serif;
    font-weight: 400;
    color: var(--ink);
    margin: 0;
    white-space: nowrap;
  }
  .card--front .wordmark {
    top: 118px;
    font-size: 26px;
    letter-spacing: 0.5px;
  }
  .card--back .wordmark {
    top: 174px;
    font-size: 33px;
    letter-spacing: 0.5px;
  }

  .divider {
    position: absolute;
    left: 30px;
    right: 28px;
    top: 168px;
    height: 0;
    border-top: 1px solid var(--rule);
  }

  .contact-person {
    position: absolute;
    left: 30px;
    top: 178px;
    font-family: "Open Sans", "Myriad Pro", sans-serif;
    font-size: 12px;
    line-height: 16px;
  }
  .contact-person .person-name {
    font-size: 15px;
    font-weight: 600;
    letter-spacing: 0.2px;
    line-height: 19px;
    text-transform: uppercase;
  }

  .contact-lines {
    position: absolute;
    right: 23px;
    top: 193px;
    font-family: "Open Sans", "Myriad Pro", sans-serif;
    font-size: 12px;
    line-height: 16px;
    text-align: right;
  }
  .contact-line {
    display: flex;
    justify-content: flex-end;
    align-items: center;
    gap: 5px;
  }
  .contact-line svg {
    width: 9px;
    height: 9px;
    flex: none;
  }
</style>
</head>
<body>
<div class="canvas">

  <section class="card card--front" aria-label="Business card front">
    <h1 class="wordmark">Brightvale Wellness</h1>
    <div class="divider"></div>

    <div class="contact-person">
      <div class="person-name">Dara Whitfield</div>
      <div>Managing Director</div>
      <div>248 Dunmore Ave E</div>
      <div>Toronto, ON K7R 3T8</div>
    </div>

    <div class="contact-lines">
      <div class="contact-line">
        <span>888 555 0142</span>
        <svg viewBox="0 0 10 10" aria-hidden="true">
          <rect x="2.5" y="0.5" width="5" height="9" rx="1" fill="none" stroke="#1e1a16" stroke-width="1"/>
          <line x1="4.3" y1="8" x2="5.7" y2="8" stroke="#1e1a16" stroke-width="0.8"/>
        </svg>
      </div>
      <div class="contact-line">
        <span>info@brightvalewellness.example</span>
        <svg viewBox="0 0 10 10" aria-hidden="true">
          <rect x="0.5" y="2" width="9" height="6.5" fill="#1e1a16"/>
          <polyline points="0.5,2 5,5.8 9.5,2" fill="none" stroke="#c9a377" stroke-width="0.8"/>
        </svg>
      </div>
      <div class="contact-line">
        <span>www.brightvalewellness.example</span>
        <svg viewBox="0 0 10 10" aria-hidden="true">
          <circle cx="5" cy="5" r="4.5" fill="#1e1a16"/>
          <ellipse cx="5" cy="5" rx="1.8" ry="4.5" fill="none" stroke="#c9a377" stroke-width="0.6"/>
          <line x1="0.5" y1="5" x2="9.5" y2="5" stroke="#c9a377" stroke-width="0.6"/>
        </svg>
      </div>
    </div>
  </section>

  <section class="card card--back" aria-label="Business card back">
    <h2 class="wordmark">Brightvale Wellness</h2>
  </section>

</div>
</body>
</html>
```